VERDALUX " need somthing eye catching and envirnmental friendely materials

Business Card " UNIQUE..
- use the agreed on logo.
- use wooden background.
- the environmental sound should be HIGH.

Company slogan is ZERO DISCHARGE.
We work in deploying the latest technology “ USA & Europe” in the field of drill cutting recycle and economically managing the footprint.
With the ramp up in oil demands and the increase in oil prices , operators are extending their operations into new geographical areas “ government regulations and eco-sounds” created the need to a specialty services and products that should go parallel or even ahead.

Target Market(s)

OIL field and environmental concerned.
Mainly ENGINEERS.

Industry/Entity Type

Government

Font styles to use
Decorative
Script

Colors

Designer to choose colors to be used in the design.

Requirements
Must have
• Eco - sounded.

```html
<!DOCTYPE html>
<html lang="en">
<head>
<meta charset="utf-8">
<title>VERDALUX Business Card</title>
<link rel="stylesheet" href="https://fonts.googleapis.com/css2?family=Cormorant+Garamond:wght@500;600&display=swap">
<style>
  :root {
    --page: #ffffff;
    --wood-light: #e9c084;
    --wood-mid: #dcaa68;
    --wood-dark: #c58d4c;
    --grain: rgba(150, 92, 38, 0.22);
    --grain-soft: rgba(150, 92, 38, 0.1);
    --paper: #ffffff;
    --ink: #3a3a3a;
    --ink-soft: #4a3a28;
    --accent: #c98b3c;
    --brand: #3f7d2a;
  }
  * { margin: 0; padding: 0; box-sizing: border-box; }
  html, body {
    width: 1200px;
    height: 1052px;
    overflow: hidden;
    background: var(--page);
    font-family: "Cormorant Garamond", Georgia, serif;
  }
  .sheet {
    width: 1200px;
    height: 1052px;
    display: flex;
    align-items: center;
    justify-content: center;
    gap: 60px;
  }
  .card {
    width: 500px;
    height: 286px;
    position: relative;
    overflow: hidden;
    box-shadow: 3px 4px 6px rgba(0,0,0,0.45);
  }
  .wood {
    position: absolute;
    inset: 0;
    background:
      repeating-linear-gradient(92deg, transparent 0 9px, var(--grain) 9px 10px, transparent 10px 23px, var(--grain-soft) 23px 25px, transparent 25px 41px),
      repeating-linear-gradient(88deg, transparent 0 31px, var(--grain-soft) 31px 33px, transparent 33px 57px),
      radial-gradient(ellipse 60px 26px at 30% 78%, rgba(160,100,40,0.25), transparent 70%),
      radial-gradient(ellipse 50px 22px at 78% 22%, rgba(160,100,40,0.2), transparent 70%),
      linear-gradient(100deg, rgba(255,255,255,0.1) 0%, rgba(0,0,0,0.06) 30%, rgba(255,255,255,0.12) 55%, rgba(0,0,0,0.08) 80%, rgba(255,255,255,0.06) 100%),
      linear-gradient(180deg, var(--wood-light), var(--wood-mid) 55%, var(--wood-dark));
  }
  /* Front */
  .card-front .brand {
    position: absolute;
    inset: 0;
    display: flex;
    align-items: center;
    justify-content: center;
    gap: 14px;
  }
  .brand-dot {
    width: 22px;
    height: 22px;
    border-radius: 50%;
    background: var(--brand);
  }
  .brand-name {
    font-size: 40px;
    font-weight: 600;
    letter-spacing: 4px;
    color: var(--brand);
  }
  /* Back */
  .card-back .identity {
    position: absolute;
    left: 0; top: 0; bottom: 0;
    width: 246px;
    background: var(--paper);
    padding: 116px 0 0 18px;
  }
  .person-name {
    font-size: 18px;
    font-weight: 500;
    color: var(--ink);
    letter-spacing: 0.3px;
    text-transform: uppercase;
    white-space: nowrap;
  }
  .person-title {
    font-size: 16px;
    font-weight: 500;
    color: var(--accent);
    padding-left: 30px;
    margin-top: -2px;
    white-space: nowrap;
  }
  .card-back .wood { left: 246px; }
  .contact {
    position: absolute;
    left: 270px;
    top: 104px;
    list-style: none;
    font-size: 15px;
    font-weight: 500;
    line-height: 1.3;
    color: var(--ink-soft);
    white-space: nowrap;
  }
</style>
</head>
<body>
  <main class="sheet">
    <section class="card card-front" aria-label="Card front">
      <div class="wood" role="img" aria-label="Light maple wood grain texture"></div>
      <div class="brand">
        <span class="brand-dot"></span>
        <span class="brand-name">VERDALUX</span>
      </div>
    </section>

    <section class="card card-back" aria-label="Card back">
      <div class="identity">
        <p class="person-name">Karim Nabil Hadad</p>
        <p class="person-title">Chief Executive Officer</p>
      </div>
      <div class="wood" role="img" aria-label="Light maple wood grain texture"></div>
      <ul class="contact">
        <li>it@verdalux.com</li>
        <li>www.verdalux.ae</li>
        <li>cell&nbsp; 009715 555 012 34</li>
      </ul>
    </section>
  </main>
</body>
</html>
```